BrimWay

This app is built around three game modes—Quick Focus, Daily, and Calming—each offering short, low-stress interactions designed to prime focus, train cognitive skills, or regulate anxiety using neuroscience-informed mechanics. Gameplay spans spatial puzzles, word and memory challenges, and breathing or sensory experiences, all delivered in 1–5 minute routines with clean, calming UI patterns (grids, cards, breathing rings, soft animations). The goal is a cohesive system of micro-games and guided routines that enhance executive function, emotional regulation, and readiness before, during, or after high-stakes moments.

Colors
FFC000
F8CF3A
FAE287
FDF2CF
FEFAEE
F0912C
F2A743
F7CA91
FBE8D2
FDF5EE
EE7325
F08F49
F5BC92
FAE3D3
FDF4ED

```html
<!DOCTYPE html>
<html lang="en">
<head>
<meta charset="utf-8">
<title>BrimWay – focus micro-games</title>
<link rel="stylesheet" href="https://fonts.googleapis.com/css2?family=Inter:wght@400;500;600&display=swap">
<style>
:root{
  --canvas:#ffffff;
  --night-top:#1f2a6b;
  --night-mid:#2a2f7a;
  --night-low:#3a2a7a;
  --ink:#ffffff;
  --ink-soft:#c9d2f2;
  --gold:#ffc000;
  --gold-soft:#f8cf3a;
  --orange:#f0912c;
  --ember:#ee7325;
  --cyan:#37d3f0;
  --cyan-deep:#0bb8f0;
  --tile:#21468e;
  --tile-hi:#2b5aa8;
  --board:#1b2f76;
  --bar:#1a2766;
}
*{box-sizing:border-box;margin:0;padding:0}
html,body{width:1200px;height:581px;overflow:hidden;background:var(--canvas);font-family:"Inter",sans-serif;color:var(--ink)}
.screen{position:absolute;top:17px;width:283px;height:547px;overflow:hidden;
  background:
   linear-gradient(180deg,transparent 0 40%,rgba(120,200,255,.18) 51%,transparent 53%),
   linear-gradient(180deg,transparent 0 88%,rgba(80,170,255,.12) 89%,transparent 90%),
   radial-gradient(ellipse at 50% 45%,rgba(140,90,220,.35),transparent 65%),
   linear-gradient(180deg,var(--night-top),var(--night-mid) 55%,var(--night-low));}
.screen--home{left:13px}.screen--matrix{left:311px}.screen--connect{left:607px}.screen--breath{left:904px}
.abs{position:absolute}
.app-name{left:14px;top:22px;font-size:16px;font-weight:500}
.avatar{left:240px;top:11px;width:27px;height:27px;border-radius:50%;border:2px solid #fff;background:radial-gradient(circle at 50% 40%,#e8c9b4,#9b6e5a)}
.streak-ring{left:56px;top:72px}
.streak-label{left:0;width:283px;top:98px;text-align:center;font-size:13px}
.streak-num{left:0;width:283px;top:118px;text-align:center;font-size:44px;font-weight:400;line-height:1}
.pill{border:1px solid var(--gold-soft);border-radius:16px;display:flex;align-items:center;justify-content:center;font-size:10.5px;color:var(--ink)}
.pill--solid{background:linear-gradient(180deg,#3ec6f2,#1a78d8);border-color:var(--gold);box-shadow:0 0 8px rgba(60,190,255,.5)}
.pill--ghost{background:rgba(20,28,90,.5)}
.focus-ready{left:92px;top:163px;width:99px;height:30px}
.mode-card{top:261px;width:79px;height:74px;border-radius:12px;border:1px solid rgba(240,145,44,.75);border-top-color:rgba(255,255,255,.3);background:linear-gradient(180deg,#25337c,#1d2660);display:flex;flex-direction:column;align-items:center;justify-content:center;gap:7px;font-size:10px}
.mode-card svg{width:26px;height:26px}
.continue{left:68px;top:374px;width:147px;height:30px}
.tagline{left:0;width:283px;top:418px;text-align:center;font-size:11px}
.bar{left:14px;top:489px;width:254px;height:37px;border-radius:19px;border:1px solid rgba(255,255,255,.55);background:rgba(18,26,85,.6);display:flex;align-items:center;justify-content:space-around;padding:0 10px}
.bar--controls{justify-content:space-between;padding:0 14px}
.bar svg{width:20px;height:20px}
.back{left:15px;top:24px;width:17px;height:17px}
.game-title{left:0;width:283px;top:22px;text-align:center;font-size:17px}
.meta{right:14px;top:27px;font-size:9.5px;display:flex;align-items:center;gap:3px}
.board{left:14px;top:111px;width:254px;height:270px;border-radius:14px;border:1px solid rgba(240,145,44,.7);border-top-color:rgba(255,255,255,.25);background:linear-gradient(180deg,#1e3c86,#1a2a6c)}
.grid{position:absolute;left:14px;top:16px;display:grid;grid-template-columns:repeat(5,44px);grid-auto-rows:44px;gap:1.5px}
.cell{background:linear-gradient(180deg,var(--tile-hi),var(--tile));border:1px solid rgba(120,170,255,.2);display:flex;align-items:center;justify-content:center}
.cell--void{background:transparent;border-color:transparent}
.c-teal{background:#3de8e0}.c-salmon{background:linear-gradient(180deg,#fb9e86,#f07e6a)}
.c-cyan{background:#0ac4f7}.c-moss{background:#93b75a}.c-violet{background:linear-gradient(180deg,#8a6fe6,#5f4ec6)}
.cell svg{width:30px;height:30px}
.btn-play{left:64px;top:405px;width:60px;height:30px}
.btn-pause{left:143px;top:405px;width:76px;height:30px}
.breath-rings{left:0;top:120px}
.btn-inhale{left:42px;top:408px;width:89px;height:30px}
.btn-exhale{left:146px;top:408px;width:94px;height:30px}
</style>
</head>
<body>
<svg width="0" height="0" style="position:absolute">
  <defs>
    <symbol id="flower" viewBox="0 0 30 30">
      <g fill="#4aa8f2" stroke="#1f6fc4" stroke-width=".6">
        <circle cx="15" cy="7.5" r="5"/><circle cx="22" cy="12.5" r="5"/><circle cx="19.5" cy="21" r="5"/>
        <circle cx="10.5" cy="21" r="5"/><circle cx="8" cy="12.5" r="5"/>
      </g><circle cx="15" cy="15" r="3.6" fill="#ffc000"/>
    </symbol>
    <symbol id="drop" viewBox="0 0 30 30">
      <path d="M15 3C11 10 7.5 14.5 7.5 19a7.5 7.5 0 0015 0C22.5 14.5 19 10 15 3z" fill="#3aa9ee"/>
      <path d="M11 18c0-2 1-4 2.5-6" stroke="#bfe7ff" stroke-width="1.3" fill="none" stroke-linecap="round"/>
    </symbol>
    <symbol id="leaf" viewBox="0 0 30 30">
      <path d="M15 2C8 9 7 16 9 21c1.5 3.5 4 6 6 7 2-1 4.5-3.5 6-7 2-5 1-12-6-19z" fill="#4caf3a"/>
      <path d="M15 6v21" stroke="#2c7a22" stroke-width="1"/>
    </symbol>
    <symbol id="coin" viewBox="0 0 30 30">
      <circle cx="15" cy="15" r="11.5" fill="#f2a743" /><circle cx="15" cy="15" r="9" fill="#ffc000"/>
      <circle cx="15" cy="15" r="5" fill="none" stroke="#f0912c" stroke-width="1"/>
    </symbol>
    <symbol id="back" viewBox="0 0 20 20">
      <circle cx="10" cy="10" r="9" fill="none" stroke="#fff" stroke-width="1.3"/>
      <path d="M14 10H6.5M9.5 6.5L6 10l3.5 3.5" fill="none" stroke="#fff" stroke-width="1.3" stroke-linecap="round" stroke-linejoin="round"/>
    </symbol>
    <symbol id="speaker" viewBox="0 0 14 12">
      <path d="M1 4h3l4-3v10L4 8H1z" fill="#fff"/>
      <path d="M10 3.5a3.5 3.5 0 010 5M11.5 2a5.5 5.5 0 010 8" stroke="#fff" fill="none" stroke-width="1.1"/>
    </symbol>
    <symbol id="pause-dot" viewBox="0 0 20 20">
      <circle cx="10" cy="10" r="9.5" fill="#3ec6f2"/><rect x="7" y="6" width="2" height="8" fill="#12205e"/><rect x="11" y="6" width="2" height="8" fill="#12205e"/>
    </symbol>
    <symbol id="power" viewBox="0 0 20 20">
      <circle cx="10" cy="10" r="9.5" fill="#3ec6f2"/>
      <path d="M7 7.2a4.2 4.2 0 106 0" fill="none" stroke="#12205e" stroke-width="1.6" stroke-linecap="round"/>
      <path d="M10 5v5" stroke="#12205e" stroke-width="1.6" stroke-linecap="round"/>
    </symbol>
  </defs>
</svg>

<!-- Home -->
<section class="screen screen--home">
  <div class="abs app-name">BrimWay</div>
  <div class="abs avatar" role="img" aria-label="User profile photo"></div>
  <svg class="abs streak-ring" width="172" height="172" viewBox="0 0 172 172">
    <defs>
      <linearGradient id="ringGrad" x1="0" y1="0" x2="1" y2="1">
        <stop offset="0" stop-color="#f0912c"/><stop offset=".5" stop-color="#6fd6e8"/><stop offset="1" stop-color="#37d3f0"/>
      </linearGradient>
    </defs>
    <circle cx="86" cy="86" r="84" fill="none" stroke="rgba(255,255,255,.35)" stroke-width="1"/>
    <circle cx="86" cy="86" r="75" fill="rgba(25,35,100,.35)" stroke="url(#ringGrad)" stroke-width="2"/>
    <path d="M14 66A74 74 0 0086 160" fill="none" stroke="#f0912c" stroke-width="2"/>
  </svg>
  <div class="abs streak-label">Strek</div>
  <div class="abs streak-num">7</div>
  <div class="abs pill pill--ghost focus-ready">Focus Ready</div>

  <div class="abs mode-card" style="left:14px">
    <svg viewBox="0 0 26 26"><circle cx="12" cy="14" r="10" fill="none" stroke="#37d3f0" stroke-width="2.2"/><circle cx="12" cy="14" r="5.5" fill="none" stroke="#37d3f0" stroke-width="2.2"/><circle cx="12" cy="14" r="1.8" fill="#37d3f0"/><path d="M12 14L22 4M19 3h4v4" stroke="#37d3f0" stroke-width="2" fill="none" stroke-linecap="round"/></svg>
    Quick Focus
  </div>
  <div class="abs mode-card" style="left:102px">
    <svg viewBox="0 0 26 26"><rect x="3" y="3" width="16" height="18" rx="2" fill="#37d3f0"/><rect x="7" y="3" width="8" height="6" fill="#1d2660"/><rect x="7" y="13" width="8" height="5" fill="#1d2660"/><path d="M17 17a4 4 0 017-1M24 20a4 4 0 01-7 1" stroke="#37d3f0" stroke-width="1.8" fill="none"/></svg>
    Daily
  </div>
  <div class="abs mode-card" style="left:190px">
    <svg viewBox="0 0 26 26"><path d="M13 3c3 3 3 8 0 11-3-3-3-8 0-11zM4 7c4 0 7 3 8 7-4 0-7-3-8-7zM22 7c-4 0-7 3-8 7 4 0 7-3 8-7z" fill="#37d3f0"/><rect x="3" y="16" width="20" height="3" rx="1.5" fill="#37d3f0"/><rect x="6" y="21" width="14" height="3" rx="1.5" fill="#37d3f0"/></svg>
    Calming
  </div>

  <div class="abs pill pill--solid continue">Continue Last Session</div>
  <div class="abs tagline">→ Two minutes to lock in.</div>

  <nav class="abs bar">
    <svg viewBox="0 0 20 20"><path d="M2 10L10 3l8 7h-2.5v7H12v-5H8v5H4.5v-7z" fill="#3ec6f2"/></svg>
    <svg viewBox="0 0 20 20"><rect x="2" y="2" width="8" height="8" rx="1.5" fill="#3ec6f2"/><rect x="10" y="10" width="8" height="8" rx="1.5" fill="#3ec6f2"/><circle cx="4.5" cy="4.5" r="1" fill="#12205e"/><circle cx="7.5" cy="7.5" r="1" fill="#12205e"/><circle cx="14" cy="14" r="1.2" fill="#12205e"/></svg>
    <svg viewBox="0 0 20 20"><circle cx="10" cy="10" r="8" fill="none" stroke="#3ec6f2" stroke-width="1.8"/><circle cx="10" cy="10" r="5" fill="none" stroke="#3ec6f2" stroke-width="1.2"/><path d="M10 7v3l2 1.5" stroke="#3ec6f2" stroke-width="1.4" fill="none"/></svg>
    <svg viewBox="0 0 20 20"><rect x="4" y="2" width="12" height="16" rx="1.5" fill="#3ec6f2"/><path d="M10 6l1 2.5 2.5 1-2.5 1-1 2.5-1-2.5-2.5-1 2.5-1z" fill="#12205e"/></svg>
    <svg viewBox="0 0 20 20"><circle cx="10" cy="6" r="4" fill="#3ec6f2"/><path d="M3 19c0-5 3-8 7-8s7 3 7 8z" fill="#3ec6f2"/></svg>
  </nav>
</section>

<!-- Mind Matrix -->
<section class="screen screen--matrix">
  <svg class="abs back"><use href="#back"/></svg>
  <div class="abs game-title">Mind Matrix</div>
  <div class="abs meta">~2min <svg width="13" height="11"><use href="#speaker"/></svg></div>
  <div class="abs board">
    <div class="grid">
      <div class="cell"></div><div class="cell"></div><div class="cell"></div><div class="cell c-teal"></div><div class="cell"></div>
      <div class="cell"></div><div class="cell c-salmon"></div><div class="cell c-salmon"></div><div class="cell c-cyan"></div><div class="cell"></div>
      <div class="cell"></div><div class="cell c-moss"></div><div class="cell c-cyan"></div><div class="cell cell--void"></div><div class="cell"></div>
      <div class="cell"></div><div class="cell"></div><div class="cell c-violet"></div><div class="cell c-salmon"></div><div class="cell cell--void"></div>
      <div class="cell"></div><div class="cell"></div><div class="cell"></div><div class="cell cell--void"></div><div class="cell cell--void"></div>
    </div>
  </div>
  <div class="abs pill pill--solid btn-play">Play</div>
  <div class="abs pill pill--ghost btn-pause">Pause</div>
  <div class="abs bar bar--controls"><svg><use href="#pause-dot"/></svg><svg><use href="#power"/></svg></div>
</section>

<!-- Calm Connect -->
<section class="screen screen--connect">
  <svg class="abs back"><use href="#back"/></svg>
  <div class="abs game-title">Calm Connect</div>
  <div class="abs meta">3:21 <svg width="13" height="11"><use href="#speaker"/></svg></div>
  <div class="abs board">
    <div class="grid">
      <div class="cell"><svg><use href="#flower"/></svg></div><div class="cell"><svg><use href="#drop"/></svg></div><div class="cell"><svg><use href="#leaf"/></svg></div><div class="cell"><svg><use href="#drop"/></svg></div><div class="cell"><svg><use href="#drop"/></svg></div>
      <div class="cell"><svg><use href="#coin"/></svg></div><div class="cell"><svg><use href="#flower"/></svg></div><div class="cell"><svg><use href="#leaf"/></svg></div><div class="cell"><svg><use href="#flower"/></svg></div><div class="cell"><svg><use href="#leaf"/></svg></div>
      <div class="cell"><svg><use href="#drop"/></svg></div><div class="cell"><svg><use href="#coin"/></svg></div><div class="cell"><svg><use href="#flower"/></svg></div><div class="cell"><svg><use href="#drop"/></svg></div><div class="cell"><svg><use href="#coin"/></svg></div>
      <div class="cell"><svg><use href="#coin"/></svg></div><div class="cell"><svg><use href="#leaf"/></svg></div><div class="cell"><svg><use href="#coin"/></svg></div><div class="cell"><svg><use href="#flower"/></svg></div><div class="cell"><svg><use href="#leaf"/></svg></div>
      <div class="cell"><svg><use href="#drop"/></svg></div><div class="cell"><svg><use href="#flower"/></svg></div><div class="cell"><svg><use href="#coin"/></svg></div><div class="cell"><svg><use href="#leaf"/></svg></div><div class="cell"><svg><use href="#flower"/></svg></div>
    </div>
  </div>
  <div class="abs pill pill--solid btn-play" style="top:403px;width:57px">Play</div>
  <div class="abs pill pill--ghost btn-pause" style="top:403px">Pause</div>
  <div class="abs bar bar--controls"><svg><use href="#pause-dot"/></svg><svg><use href="#power"/></svg></div>
</section>

<!-- Breath Beats -->
<section class="screen screen--breath">
  <svg class="abs back"><use href="#back"/></svg>
  <div class="abs game-title">Breath Beats</div>
  <div class="abs meta">~2min <svg width="13" height="11"><use href="#speaker"/></svg></div>
  <svg class="abs breath-rings" width="283" height="260" viewBox="0 0 283 260">
    <defs>
      <linearGradient id="waveGrad" x1="0" x2="1"><stop offset="0" stop-color="#5fb6d8"/><stop offset=".5" stop-color="#ffffff"/><stop offset="1" stop-color="#37d3f0"/></linearGradient>
    </defs>
    <circle cx="143" cy="127" r="128" fill="none" stroke="rgba(255,255,255,.18)" stroke-width="1"/>
    <circle cx="143" cy="127" r="113" fill="rgba(30,40,110,.25)" stroke="#37d3f0" stroke-width="1.6"/>
    <path d="M30 127A113 113 0 01143 14" fill="none" stroke="#fff" stroke-width="1.4" opacity=".8"/>
    <circle cx="143" cy="127" r="92" fill="none" stroke="rgba(255,255,255,.7)" stroke-width="1.2"/>
    <circle cx="143" cy="127" r="92" fill="none" stroke="#37d3f0" stroke-width="1" stroke-dasharray="200 400" transform="rotate(60 143 127)"/>
    <path d="M0 130C40 118 80 140 105 138C125 136 130 93 148 93C165 93 172 145 190 140C215 134 245 118 283 124" fill="none" stroke="url(#waveGrad)" stroke-width="3" stroke-linecap="round"/>
  </svg>
  <div class="abs pill pill--solid btn-inhale">Start Inhale</div>
  <div class="abs pill pill--ghost btn-exhale">Stop Exhale</div>
  <div class="abs bar bar--controls"><svg><use href="#pause-dot"/></svg><svg><use href="#power"/></svg></div>
</section>
</body>
</html>
```